TQR Habitat Stewards 2019

We need a 2 page flyer to advertise our upcoming program. The program covers 5 months May-September 2019 and is focused on conservation.I have attached some options that i like. It needs to be striking.

Text in newly uploaded document 'HSFlyer2'

Target Market(s)

Conservation
Conscious travelers
30-45 year olds
Environmental
Adventure/Hiking
Citizen Science

Font styles to use
Sans Serif

Colors
0355a3
fbed22

Requirements
Must have
• A travel conservation focus
• Highlight the significance of the 'in the world' status of the project
Nice to have
• A yellow border, making it look similar to the cover of Wanderfield Quarterly

```html
<!DOCTYPE html>
<html lang="en">
<head>
<meta charset="utf-8">
<title>TQR Habitat Stewards 2019 – Flyer</title>
<link rel="stylesheet" href="https://fonts.googleapis.com/css2?family=Poppins:wght@400;500;600;700;800&display=swap">
<style>
  :root {
    --brand-blue: #0355a3;
    --brand-yellow: #fbed22;
    --deep-blue: #0a3f8f;
    --sky-top: #7fb3dc;
    --sky-low: #cfe3f1;
    --sea: #2f78b8;
    --hill: #4d6b35;
    --stage: #e4e6e8;
    --ink-dark: #1d1d1d;
    --white: #ffffff;
  }
  * { margin: 0; padding: 0; box-sizing: border-box; }
  html, body { width: 1200px; height: 849px; overflow: hidden; }
  body { background: var(--stage); font-family: 'Poppins', sans-serif; position: relative; }

  .page { position: absolute; top: 24px; height: 802px; background: var(--brand-yellow); }
  .page--cover { left: 22px; width: 567px; }
  .page--schedule { left: 612px; width: 567px; }

  /* Cover */
  .cover-photo {
    position: absolute; left: 21px; top: 22px; width: 525px; height: 756px;
    background: linear-gradient(180deg, var(--sky-top) 0%, var(--sky-low) 42%, var(--sea) 52%, #3f7a4a 62%, var(--hill) 78%, #8f8a76 100%);
  }
  .brand-mark { position: absolute; left: 46px; top: 60px; width: 120px; display: flex; align-items: center; gap: 8px; }
  .brand-mark__dot { width: 16px; height: 16px; border-radius: 50%; background: var(--brand-blue); flex: none; }
  .brand-mark__name { color: var(--brand-blue); font-weight: 700; font-size: 15px; line-height: 1.15; }

  .cover-title { position: absolute; left: 204px; top: 50px; color: var(--brand-blue); font-weight: 700; font-size: 46px; line-height: 48px; letter-spacing: 0.5px; }
  .cover-year { position: absolute; left: 204px; top: 146px; color: var(--white); font-weight: 700; font-size: 76px; line-height: 76px; }

  .sessions { position: absolute; left: 112px; top: 224px; width: 333px; height: 106px; border: 3px solid var(--brand-blue); color: var(--brand-blue); }
  .sessions__head { height: 46px; border-bottom: 3px solid var(--brand-blue); text-align: center; font-weight: 800; font-size: 26px; letter-spacing: 9px; line-height: 44px; }
  .sessions__row { display: flex; height: 54px; }
  .sessions__count { width: 165px; border-right: 3px solid var(--brand-blue); display: flex; align-items: center; padding-left: 22px; gap: 8px; }
  .sessions__num { font-weight: 700; font-size: 48px; line-height: 1; }
  .sessions__unit { font-weight: 600; font-size: 18px; }
  .sessions__range { flex: 1; display: flex; align-items: center; justify-content: center; font-weight: 600; font-size: 18px; }

  .visit-bar { position: absolute; left: 50px; top: 693px; width: 466px; height: 57px; background: rgba(3, 85, 163, 0.85); display: flex; align-items: center; justify-content: center; gap: 10px; }
  .visit__label { color: var(--brand-yellow); font-size: 21px; font-weight: 500; }
  .visit__url { color: var(--white); font-size: 21px; font-weight: 500; }
  .visit__icon { width: 14px; height: 14px; }

  /* Schedule page */
  .schedule-top { position: absolute; left: 22px; top: 22px; width: 545px; height: 316px; background: linear-gradient(180deg, #dcdcdc 0%, #c9c9c9 55%, #e2e2e2 100%); }
  .schedule-top__tab { position: absolute; left: 292px; top: 0; width: 275px; height: 22px; background: #d4d4d4; }
  .schedule-bottom { position: absolute; left: 0; top: 373px; width: 546px; height: 405px; background: linear-gradient(180deg, #0a56b4 0%, #1a6cc4 45%, #2e79bd 60%, #0b4aa0 85%, var(--deep-blue) 100%); }
  .schedule-bottom__tab { position: absolute; left: 0; top: 778px; width: 350px; height: 24px; background: var(--deep-blue); }

  .month { position: absolute; text-align: center; }
  .month__tag { display: inline-block; border: 2px solid; font-weight: 700; font-size: 20px; line-height: 25px; padding: 0 14px; }
  .month__text { font-size: 13.6px; line-height: 16px; }
  .month--light .month__tag { color: var(--brand-blue); border-color: var(--brand-blue); background: var(--white); }
  .month--light .month__text { color: var(--ink-dark); }
  .month--dark .month__tag { color: var(--brand-yellow); border-color: var(--brand-yellow); }
  .month--dark .month__text { color: var(--white); }

  .visit--footer { position: absolute; left: 22px; top: 752px; display: flex; align-items: center; gap: 8px; }
  .visit--footer .visit__label, .visit--footer .visit__url { font-size: 18px; }
</style>
</head>
<body>

<section class="page page--cover">
  <div class="cover-photo" role="img" aria-label="Photo of two hikers on a rocky clifftop overlooking a green island coastline and blue sea, with seabirds in the sky"></div>

  <div class="brand-mark">
    <span class="brand-mark__dot"></span>
    <span class="brand-mark__name">TQR Habitat Stewards</span>
  </div>

  <h1 class="cover-title">HABITAT<br>STEWARDS</h1>
  <div class="cover-year">2019</div>

  <div class="sessions">
    <div class="sessions__head">SESSIONS</div>
    <div class="sessions__row">
      <div class="sessions__count"><span class="sessions__num">5</span><span class="sessions__unit">Months</span></div>
      <div class="sessions__range">May-September</div>
    </div>
  </div>

  <div class="visit-bar">
    <span class="visit__label">Visit us</span>
    <svg class="visit__icon" viewBox="0 0 16 16" fill="none" stroke="#fbed22" stroke-width="1.4"><circle cx="8" cy="8" r="7"/><ellipse cx="8" cy="8" rx="3" ry="7"/><path d="M1 8h14M2.5 4.5h11M2.5 11.5h11"/></svg>
    <span class="visit__url">www.tqrhabitat.info</span>
  </div>
</section>

<section class="page page--schedule">
  <div class="schedule-top__tab"></div>
  <div class="schedule-top" role="img" aria-label="Faded grey photo of a steep mountain peak"></div>
  <div class="schedule-bottom" role="img" aria-label="Aerial photo of an island and lagoon in a deep blue ocean"></div>
  <div class="schedule-bottom__tab"></div>

  <div class="month month--light" style="left:34px; top:54px; width:514px;">
    <span class="month__tag" style="width:94px;">MAY</span>
    <p class="month__text" style="margin-top:22px;">Apart from counting words and characters, our online editor can help you to improve word choice and writing style, and, optionally, help you to detect grammar mistakes and plagiarism. To check word count, simply place your cursor into the text box above and start typing.</p>
  </div>

  <div class="month month--light" style="left:34px; top:197px; width:514px;">
    <span class="month__tag" style="width:94px;">JUNE</span>
    <p class="month__text" style="margin-top:22px;">Apart from counting words and characters, our online editor can help you to improve word choice and writing style, and, optionally, help you to detect grammar mistakes and plagiarism. To check word count, simply place your cursor into the text box above and start typing.</p>
  </div>

  <div class="month month--dark" style="left:12px; top:401px; width:252px;">
    <span class="month__tag" style="width:94px;">JULY</span>
    <p class="month__text" style="margin-top:22px;">Apart from counting words and characters, our online editor can help you to improve word choice and writing style, and, optionally, help you to detect grammar mistakes and plagiarism. To check word count, simply place your cursor into the text box above and start typing.</p>
  </div>

  <div class="month month--dark" style="left:278px; top:401px; width:252px;">
    <span class="month__tag" style="width:118px;">AUGUST</span>
    <p class="month__text" style="margin-top:22px;">Apart from counting words and characters, our online editor can help you to improve word choice and writing style, and, optionally, help you to detect grammar mistakes and plagiarism. To check word count, simply place your cursor into the text box above and start typing.</p>
  </div>

  <div class="month month--dark" style="left:20px; top:614px; width:512px;">
    <span class="month__tag" style="width:144px;">SEPTEMBER</span>
    <p class="month__text" style="margin-top:22px;">Apart from counting words and characters, our online editor can help you to improve word choice and writing style, and, optionally, help you to detect grammar mistakes and plagiarism. To check word count, simply place your cursor into the text box above and start typing.</p>
  </div>

  <div class="visit--footer">
    <span class="visit__label">Visit us</span>
    <svg class="visit__icon" viewBox="0 0 16 16" fill="none" stroke="#fbed22" stroke-width="1.4"><circle cx="8" cy="8" r="7"/><ellipse cx="8" cy="8" rx="3" ry="7"/><path d="M1 8h14M2.5 4.5h11M2.5 11.5h11"/></svg>
    <span class="visit__url">www.tqrhabitat.info</span>
  </div>
</section>

</body>
</html>
```